Mortgage broker flyer

I need a flyer to advertise who we are, what we do and why people should use us. and with a call to action. Our service is free, and we have over 35 different lenders that we can source loans from. we offer a mobile service. we will visit people anywhere anytime to discuss their needs. The flyers are to be placed in real estate agencies as well as put in people's letter boxes

Target Market(s)

clients looking at purchasing property - going through open homes.

Industry/Entity Type

Finance

Colors
add136
cadf82
aaaaaa
959595

Requirements
Must have
• Service is free
• won KRD broker of the year 2014,2015
• Veltrona insurance - Free 90 days building insurance through Veltrona
• Logo colours

```html
<!DOCTYPE html>
<html lang="en">
<head>
<meta charset="utf-8">
<title>Harbour Lend Finance Group – Mortgage Broker Flyer</title>
<link rel="stylesheet" href="https://fonts.googleapis.com/css2?family=Oswald:wght@500;600&family=Source+Sans+3:wght@400;600&family=Cinzel:wght@500&display=swap">
<style>
  :root {
    --green: #add136;
    --green-light: #cadf82;
    --green-dark: #2f4a0b;
    --grey-light: #aaaaaa;
    --grey: #959595;
    --grey-text: #6e6e6e;
    --white: #ffffff;
    --ink: #1a1a1a;
  }
  * { margin: 0; padding: 0; box-sizing: border-box; }
  html, body { width: 872px; height: 1200px; overflow: hidden; background: var(--white); }
  .flyer { position: relative; width: 872px; height: 1200px; font-family: "Source Sans 3", sans-serif; }

  .header { position: absolute; left: 0; top: 0; width: 872px; height: 165px; background: var(--white); border-bottom: 6px solid var(--grey-light); }
  .brand { position: absolute; display: flex; align-items: center; gap: 22px; }
  .brand-mark { border-radius: 50%; background: var(--green); flex: none; }
  .brand-name { color: var(--green); font-weight: 400; line-height: 1; }
  .header .brand { left: 40px; top: 38px; }
  .header .brand-mark { width: 70px; height: 70px; }
  .header .brand-name { font-size: 52px; }
  .header .brand-name span { display: block; }

  .hero { position: absolute; left: 0; top: 171px; width: 872px; height: 480px; }
  .hero-photo { position: absolute; inset: 0; background: linear-gradient(120deg, #3a3d44 0%, #5d6269 35%, #c9d9da 60%, #e8eef0 100%); }
  .hero-tagline { position: absolute; right: 44px; top: 215px; text-align: right; font-family: "Oswald", sans-serif; font-weight: 600; font-size: 39px; line-height: 48px; color: var(--white); text-shadow: 0 2px 4px rgba(0,0,0,.55); }
  .hero-url { position: absolute; left: 84px; top: 430px; font-size: 24px; font-weight: 600; color: var(--ink); }
  .hero-rule { position: absolute; left: 0; bottom: 0; width: 872px; height: 8px; background: var(--green); }
  .mobile-tab { position: absolute; right: 34px; bottom: 0; width: 370px; height: 46px; }
  .mobile-tab span { position: absolute; inset: 0; display: flex; align-items: center; justify-content: center; font-family: "Oswald", sans-serif; font-weight: 500; font-size: 25px; color: var(--white); padding-top: 2px; }

  .details { position: absolute; left: 0; top: 651px; width: 872px; height: 456px; background: var(--grey); color: var(--white); }
  .details h2 { position: absolute; left: 88px; top: 30px; font-weight: 400; font-size: 30px; }
  .details .intro { position: absolute; left: 88px; top: 86px; width: 710px; font-size: 19px; line-height: 27px; color: #f1f1f1; }
  .benefits { position: absolute; left: 88px; top: 216px; list-style: none; font-family: "Oswald", sans-serif; font-weight: 500; font-size: 23px; }
  .benefits li { display: flex; align-items: center; gap: 12px; height: 35px; }
  .benefits svg { width: 20px; height: 20px; flex: none; }
  .audience { position: absolute; left: 90px; top: 332px; width: 702px; height: 38px; border-radius: 19px; background: var(--green); color: var(--green-dark); font-weight: 600; font-size: 19px; display: flex; align-items: center; justify-content: center; }
  .call { position: absolute; left: 88px; top: 384px; font-family: "Cinzel", serif; font-weight: 500; color: var(--white); white-space: nowrap; }
  .call .label { font-size: 42px; letter-spacing: 1px; }
  .call .number { font-size: 50px; margin-left: 20px; }

  .footer { position: absolute; left: 0; top: 1107px; width: 872px; height: 93px; background: var(--white); }
  .footer .brand { left: 32px; top: 22px; gap: 14px; }
  .footer .brand-mark { width: 44px; height: 44px; }
  .footer .brand-name { font-size: 30px; }
  .footer .brand-name span { display: block; }
  .footer-divider { position: absolute; left: 463px; top: 14px; width: 1px; height: 64px; background: #dddddd; }
  .contact { position: absolute; right: 40px; top: 12px; text-align: right; color: var(--ink); }
  .contact .address { font-size: 15px; line-height: 22px; }
  .contact p { font-size: 19px; line-height: 26px; }
  .contact .key { color: var(--green); }
</style>
</head>
<body>
<main class="flyer">
  <header class="header">
    <div class="brand">
      <div class="brand-mark"></div>
      <div class="brand-name"><span>Harbour Lend</span><span>Finance Group</span></div>
    </div>
  </header>

  <section class="hero">
    <div class="hero-photo" role="img" aria-label="Photo of a broker and a client at a glass desk with a small model house, a pen and loan papers"></div>
    <p class="hero-tagline">we will visit people<br>anywhere anytime<br>to discuss their needs<br>source loans from</p>
    <p class="hero-url">www.harbourlendfg.com.au</p>
    <div class="hero-rule"></div>
    <div class="mobile-tab">
      <svg width="370" height="46" viewBox="0 0 370 46">
        <path d="M0 38 L14 46 L14 38 Z" fill="#6e8a1e"/>
        <path d="M356 38 L370 38 L356 46 Z" fill="#6e8a1e"/>
        <path d="M0 38 Q22 38 30 20 Q38 0 60 0 L310 0 Q332 0 340 20 Q348 38 370 38 L356 46 L14 46 Z" fill="#add136"/>
      </svg>
      <span>we offer a mobile service</span>
    </div>
  </section>

  <section class="details">
    <h2>35 Different Lenders</h2>
    <p class="intro">Buying your first home or refinancing is a very daunting process with over 300 loan products out there, which is why at Harbour Lend Finance Group we’ll walk you through the steps from choosing the perfect loan from our home loan product range, to applying and getting approval.</p>
    <ul class="benefits">
      <li><svg viewBox="0 0 20 20"><circle cx="10" cy="10" r="8" fill="none" stroke="#fff" stroke-width="2.4"/><path d="M5.5 10 L9 13.5 L17 4" fill="none" stroke="#fff" stroke-width="3" stroke-linecap="round"/></svg>Service is free</li>
      <li><svg viewBox="0 0 20 20"><circle cx="10" cy="10" r="8" fill="none" stroke="#fff" stroke-width="2.4"/><path d="M5.5 10 L9 13.5 L17 4" fill="none" stroke="#fff" stroke-width="3" stroke-linecap="round"/></svg>won KRD broker of the year 2014,2015</li>
      <li><svg viewBox="0 0 20 20"><circle cx="10" cy="10" r="8" fill="none" stroke="#fff" stroke-width="2.4"/><path d="M5.5 10 L9 13.5 L17 4" fill="none" stroke="#fff" stroke-width="3" stroke-linecap="round"/></svg>Veltrona insurance - Free 90 days building insurance through Veltrona</li>
    </ul>
    <p class="audience">clients looking at purchasing property - going through open homes.</p>
    <p class="call"><span class="label">CALL US TODAY :</span><span class="number">07 3000 1234</span></p>
  </section>

  <footer class="footer">
    <div class="brand">
      <div class="brand-mark"></div>
      <div class="brand-name"><span>Harbour Lend</span><span>Finance Group</span></div>
    </div>
    <div class="footer-divider"></div>
    <div class="contact">
      <div class="address">Po Box 1187, Ashby. QLD. 4520</div>
      <p><span class="key">Mobile:</span> 0400 111 222</p>
      <p><span class="key">Email:</span> info@harbourlendfg.com.au</p>
    </div>
  </footer>
</main>
</body>
</html>
```